Website design for TrelWave - introducing new product set and theme

We need a design for the new website to present our extended product set, introduce the "Brisk Under Sky" theme and to promote our aim and purpose. We are expanding our product offer to cover 3 products which need clearly presented on the home page 1) TrelWave targeting families and individuals 2) TrelBind for commercial or group use in Charities or outdoor centres 3) TrelTutoring for eduction. Each product should have its own identity based on the Trel brand.

The current websites are mytrelquestly.example and mytrelwave.example. We have brochure covers, exhibition stand designs and the app itself in the app store.

Our aim is to be a leader in providing a digital platform for interactive learning for the outdoors bringing engagement and motivation to explore and realise the personal health and wellbeing benefit from experiences the outdoors. We want to provide a solution to help address the recognised issue of "Nature disorder deficit" among children today while increasing exercise and activity.
We will motivate and inspire everyone to be more active and improve the appreciation and enjoyment of the outdoors delivered through active adventures. People today from young to elderly, are less active with the knowledge, appreciation and enjoyment of the outdoors being eroded to a level that our next generation will not realise the benefits outdoor experiences will provide. TrelWave will refocus the education of the outdoors, nature and related skills introducing interactive learning utilising digital tools and solution. TrelWave's aim is to be a leader in offering innovative interactive learning and with an approach which results in us all being more active. We want more active communities across the world enjoying the natural landscapes.

A theme we want to introduce is Brisk Under Sky and intend to create a community around this. We need to consider how the Brisk Under Sky theme is brought into the design introducing an ident. The Brisk Under Sky community will be developed into a subscription-based model.

The current web site for the current myTrelQuestly mobile app (to be renamed TrelWave) itself : www.mytrelquestly.example
A temporary site was created: mytrelwave.example to start to tell the brand story.

Brand
We have a brand direction with a logo (the G ) this can be extended if required but we are not looking for a complete change. See the website and brochure page for current style, colour and fonts

Design to be clean, not cluttered and modern.

Brisk Under Sky will need an identity and it is expected that at a later date it will have its own website.

Sites in the same area and a design we admire.
https://www.pathlorn.example/
https://www.hillsprite.example/en-gb
https://www.commonheritageband.example.uk

```html
<!DOCTYPE html>
<html lang="en">
<head>
<meta charset="utf-8">
<title>TrelWave — Brisk Under Sky</title>
<link href="https://fonts.googleapis.com/css2?family=Raleway:wght@400;500;600;700&family=Rubik:wght@400;500;700&display=swap" rel="stylesheet">
<style>
:root{
  --orange:#f07c30;
  --dark:#262626;
  --ink:#1f1f1f;
  --nav-bg:#ececec;
  --white:#ffffff;
}
*{margin:0;padding:0;box-sizing:border-box}
html,body{width:1200px;height:3793px;overflow:hidden;background:var(--white)}
body{position:relative;font-family:"Raleway",sans-serif;color:var(--ink)}
.abs{position:absolute}
.shapes{position:absolute;left:0;top:0;width:1200px;height:3793px;z-index:0}
.layer{position:relative;z-index:1}

/* header */
.brand{left:88px;top:26px;display:flex;align-items:center;gap:14px}
.brand-dot{width:56px;height:56px;border-radius:50%;background:var(--orange)}
.brand-name{font-family:"Rubik",sans-serif;font-weight:500;font-size:44px;color:var(--orange);letter-spacing:.5px}
.call{left:621px;top:34px;display:flex;align-items:center;gap:10px}
.call-icon{width:40px;height:40px}
.call-text{font-family:"Rubik",sans-serif;font-size:16px;line-height:20px;color:var(--ink)}
.call-text b{display:block;color:var(--orange);font-weight:500}
.social{left:918px;top:37px;display:flex;gap:9px}
.social span{width:40px;height:40px;border-radius:50%;background:var(--orange);display:block}

.nav{left:0;top:113px;width:1200px;height:61px;background:var(--nav-bg);box-shadow:0 3px 6px rgba(0,0,0,.08)}
.nav a{position:absolute;top:20px;font-size:18.5px;letter-spacing:1.3px;color:var(--ink);text-decoration:none;font-weight:500}
.nav a.active{color:var(--orange);border-bottom:3px solid var(--orange);padding-bottom:6px}

/* buttons */
.btn{display:flex;align-items:center;justify-content:center;gap:8px;height:48px;border-radius:24px;font-family:"Rubik",sans-serif;font-weight:500;font-size:16px;color:var(--white);background:var(--orange)}
.btn.ghost{background:transparent;border:2px solid var(--orange);color:var(--orange)}
.btn svg{width:16px;height:16px}

/* hero: Brisk Under Sky theme */
.theme{left:88px;top:318px;display:flex;align-items:center;gap:14px}
.theme-ident{width:34px;height:34px;border-radius:50%;border:5px solid var(--white);flex:none}
.theme-title{font-family:"Raleway",sans-serif;font-weight:600;font-size:50px;line-height:60px;color:var(--white)}
.hero-text{left:88px;top:384px;width:440px;font-size:18px;line-height:35.5px;color:var(--white);font-weight:500}

/* section headings */
.mark{width:30px;height:30px;border-radius:50%;border:6px solid var(--orange)}
.h2{font-family:"Rubik",sans-serif;font-weight:500;color:var(--orange)}
.body-text{font-size:15.5px;line-height:36px;color:var(--ink)}

/* features */
.feature{left:563px;display:flex;align-items:center;gap:14px}
.feature-ring{width:80px;height:80px;border-radius:50%;border:3px solid var(--white);display:flex;align-items:center;justify-content:center;flex:none}
.feature-ring svg{width:40px;height:40px}
.feature-text{font-family:"Rubik",sans-serif;font-weight:500;font-size:22px;line-height:37px;color:var(--white)}

/* cards */
.card{top:2816px;width:328px}
.card-media{width:328px;height:191px}
.card-title{margin-top:22px;font-family:"Rubik",sans-serif;font-weight:500;font-size:21px;color:var(--orange)}
.card-text{margin-top:10px;font-size:12.5px;line-height:25px;color:var(--ink)}
.card-link{margin-top:8px;font-size:16px;color:var(--orange)}

/* footer */
.foot-brand{left:0;top:3412px;width:1200px;display:flex;align-items:center;justify-content:center;gap:16px}
.foot-brand .brand-dot{width:66px;height:66px}
.foot-brand .brand-name{font-size:52px}
.foot-h{font-family:"Rubik",sans-serif;font-weight:700;font-size:23px;color:var(--white);letter-spacing:.5px}
.quick li{list-style:none;font-size:15px;line-height:29px;color:var(--white)}
.quick li::before{content:"»";color:var(--white);margin-right:9px;font-size:13px}
.contact-row{display:flex;gap:14px;font-size:13px;line-height:26.5px;color:var(--white)}
.contact-row svg{width:13px;height:13px;margin-top:7px;flex:none}
.field{height:39px;border:2px solid var(--white);color:var(--white);font-size:13px;font-weight:600;padding:11px 9px}
.submit{height:39px;background:var(--orange);color:var(--white);font-size:14px;display:flex;align-items:center;justify-content:center}
.copyright{left:0;top:3742px;width:1200px;text-align:center;font-size:12px;color:var(--white)}
</style>
</head>
<body>

<svg class="shapes" viewBox="0 0 1200 3793" aria-hidden="true">
  <defs>
    <linearGradient id="heroGrad" x1="0" y1="0" x2="1" y2="1">
      <stop offset="0" stop-color="#4f5a2e"/>
      <stop offset=".35" stop-color="#6b6a3c"/>
      <stop offset=".6" stop-color="#8d8a74"/>
      <stop offset="1" stop-color="#5e5436"/>
    </linearGradient>
    <linearGradient id="heroShade" x1="0" y1="0" x2="1" y2="0">
      <stop offset="0" stop-color="#1e2410" stop-opacity=".55"/>
      <stop offset=".55" stop-color="#1e2410" stop-opacity=".15"/>
      <stop offset="1" stop-color="#1e2410" stop-opacity=".25"/>
    </linearGradient>
    <linearGradient id="sunsetGrad" x1="0" y1="0" x2="0" y2="1">
      <stop offset="0" stop-color="#4a3a4e"/>
      <stop offset=".35" stop-color="#a86a5c"/>
      <stop offset=".55" stop-color="#e09a6c"/>
      <stop offset=".75" stop-color="#5a4a3a"/>
      <stop offset="1" stop-color="#2e2a22"/>
    </linearGradient>
    <linearGradient id="orangeGrad" x1="0" y1="0" x2="0" y2="1">
      <stop offset="0" stop-color="#f08a3e"/>
      <stop offset="1" stop-color="#e8742a"/>
    </linearGradient>
    <linearGradient id="forestGrad" x1="0" y1="0" x2="0" y2="1">
      <stop offset="0" stop-color="#5a6a4e"/>
      <stop offset=".5" stop-color="#3e4a32"/>
      <stop offset="1" stop-color="#7a5a3a"/>
    </linearGradient>
    <linearGradient id="duskGrad" x1="0" y1="0" x2="0" y2="1">
      <stop offset="0" stop-color="#3a2a2a"/>
      <stop offset=".45" stop-color="#c2602a"/>
      <stop offset=".6" stop-color="#f0a040"/>
      <stop offset=".75" stop-color="#2a1e1a"/>
      <stop offset="1" stop-color="#120e0c"/>
    </linearGradient>
  </defs>

  <g role="img" aria-label="Photo: mountain bikers riding a grassy hill trail">
    <path d="M0 174 H1200 V714 L1075 739 L868 758 L692 788 L600 821 L515 788 L336 754 L132 740 L0 714 Z" fill="url(#heroGrad)"/>
    <path d="M0 174 H1200 V714 L1075 739 L868 758 L692 788 L600 821 L515 788 L336 754 L132 740 L0 714 Z" fill="url(#heroShade)"/>
  </g>
  <polyline points="0,714 132,740 336,754 515,788 600,821 692,788 868,758 1075,739 1200,714" fill="none" stroke="#f07c30" stroke-width="2.5"/>
  <g fill="#f07c30">
    <circle cx="132" cy="740" r="4"/><circle cx="515" cy="788" r="4"/>
    <circle cx="692" cy="788" r="4"/><circle cx="1075" cy="739" r="4"/>
  </g>
  <g fill="#fff" stroke="#f07c30" stroke-width="2.5">
    <circle cx="336" cy="754" r="12"/><circle cx="868" cy="758" r="12"/>
    <circle cx="600" cy="821" r="15"/>
  </g>

  <polygon points="290,901 493,1013 493,1239 290,1351 88,1239 88,1013" fill="#fff" stroke="#f07c30" stroke-width="2.5"/>
  <polygon points="290,920 478,1025 478,1228 290,1332 103,1228 103,1025" fill="url(#forestGrad)" role="img" aria-label="Photo: cyclists riding through a pine forest"/>

  <polygon points="0,1435 339,1468 442,1494 600,1538 600,2083 383,2017 177,1980 0,1958" fill="url(#sunsetGrad)" role="img" aria-label="Photo: hills at sunset"/>
  <polygon points="600,1538 765,1494 883,1465 1200,1428 1200,1965 1001,2024 824,2017 600,2083" fill="url(#orangeGrad)" role="img" aria-label="Photo: cyclist on a hill, tinted orange"/>
  <polyline points="0,1435 339,1468 442,1494 600,1538 765,1494 883,1465 1200,1428" fill="none" stroke="#f07c30" stroke-width="3"/>
  <polyline points="600,2083 824,2017 1001,2024 1200,1965" fill="none" stroke="#f07c30" stroke-width="3"/>

  <polygon points="900,2161 1101,2274 1101,2501 900,2614 698,2501 698,2274" fill="#fff" stroke="#f07c30" stroke-width="2.5"/>
  <polygon points="900,2180 1087,2286 1087,2490 900,2596 712,2490 712,2286" fill="url(#duskGrad)" role="img" aria-label="Photo: mountain biker silhouetted against a sunset"/>

  <line x1="90" y1="2691" x2="1110" y2="2691" stroke="#e4e4e4" stroke-width="1"/>

  <path d="M0 3238 L132 3260 L336 3280 L515 3312 L600 3350 L692 3312 L868 3285 L1075 3260 L1200 3238 V3793 H0 Z" fill="#262626"/>
  <polyline points="0,3238 132,3260 336,3280 515,3312 600,3350 692,3312 868,3285 1075,3260 1200,3238" fill="none" stroke="#f07c30" stroke-width="2.5"/>
  <g fill="#f07c30">
    <circle cx="132" cy="3260" r="4"/><circle cx="515" cy="3312" r="4"/>
    <circle cx="692" cy="3312" r="4"/><circle cx="1075" cy="3260" r="4"/>
  </g>
  <g fill="#fff" stroke="#f07c30" stroke-width="2.5">
    <circle cx="336" cy="3280" r="12"/><circle cx="868" cy="3285" r="12"/>
    <circle cx="600" cy="3350" r="15"/>
  </g>
</svg>

<div class="layer">
  <div class="abs brand"><span class="brand-dot"></span><span class="brand-name">TrelWave</span></div>
  <div class="abs call">
    <svg class="call-icon" viewBox="0 0 40 40"><circle cx="20" cy="20" r="18" fill="none" stroke="#f07c30" stroke-width="2.5"/><path d="M13 12c1-1 2-1 3 0l2 3c.6 1 .3 2-.5 2.6l-1 .8c1 2.3 2.8 4.1 5 5l.8-1c.6-.8 1.6-1.1 2.6-.5l3 2c1 1 1 2 0 3l-1.4 1.4c-4.5 1-13-7.5-12-12z" fill="#f07c30"/></svg>
    <div class="call-text">Call Us:<b>(555) 014 - 2730</b></div>
  </div>
  <div class="abs social" aria-label="Social links"><span></span><span></span><span></span><span></span></div>

  <nav class="abs nav">
    <a class="active" style="left:155px">HOME</a>
    <a style="left:262px">PROJECTS</a>
    <a style="left:412px">WHAT WE DO</a>
    <a style="left:590px">CONTACT</a>
    <a style="left:733px">MY TREL ADVENTURE PLATFORM</a>
  </nav>

  <div class="abs theme"><span class="theme-ident"></span><h1 class="theme-title">Brisk Under Sky</h1></div>
  <p class="abs hero-text">Join the TrelWave community getting out, moving more and enjoying the outdoors together, one adventure at a time.</p>
  <div class="abs btn" style="left:88px;top:506px;width:182px">Read More <svg viewBox="0 0 16 16"><circle cx="8" cy="8" r="8" fill="#fff"/><path d="M4 8h7M8 5l3 3-3 3" stroke="#f07c30" stroke-width="1.8" fill="none"/></svg></div>

  <div class="abs mark" style="left:523px;top:980px"></div>
  <h2 class="abs h2" style="left:523px;top:1022px;font-size:38px">Our Approach</h2>
  <p class="abs body-text" style="left:523px;top:1074px;width:600px">We give you give you tools to help you create adventures and work with others to motivate and enjoy the outdoors.<br>We will work with you to engage and create an outdoor experience which is fun and engaging for anyone you offer it to.</p>
  <div class="abs btn" style="left:523px;top:1231px;width:181px">Our Vision <svg viewBox="0 0 16 16"><circle cx="8" cy="8" r="8" fill="#fff"/><path d="M4 8h7M8 5l3 3-3 3" stroke="#f07c30" stroke-width="1.8" fill="none"/></svg></div>

  <div class="abs mark" style="left:92px;top:1580px"></div>
  <h2 class="abs h2" style="left:90px;top:1618px;font-size:38px">About Us</h2>
  <p class="abs" style="left:90px;top:1666px;width:455px;font-size:16px;line-height:36px;color:#fff;text-align:justify">Lorem ipsum dolor sit amet, consectetur adipiscing elit, sed do eiusmod tempor incididunt ut labore et dolore magna aliqua. Quis ipsum suspendisse ultrices gravida. Risus maecenas accumsan lacus vel facilisis.</p>
  <div class="abs btn" style="left:93px;top:1825px;width:181px">Read More <svg viewBox="0 0 16 16"><circle cx="8" cy="8" r="8" fill="#fff"/><path d="M4 8h7M8 5l3 3-3 3" stroke="#f07c30" stroke-width="1.8" fill="none"/></svg></div>

  <div class="abs feature" style="top:1594px">
    <span class="feature-ring"><svg viewBox="0 0 40 40"><circle cx="20" cy="13" r="7" fill="#fff"/><path d="M7 36c0-8 6-13 13-13s13 5 13 13z" fill="#fff"/></svg></span>
    <span class="feature-text">TrelWave targeting families and<br>individuals</span>
  </div>
  <div class="abs feature" style="top:1715px">
    <span class="feature-ring"><svg viewBox="0 0 40 40"><circle cx="20" cy="20" r="14" fill="none" stroke="#fff" stroke-width="3"/><path d="M20 12v9l6 4" stroke="#fff" stroke-width="3" fill="none"/></svg></span>
    <span class="feature-text">TrelBind for commercial or group use in<br>Charities or outdoor centres</span>
  </div>
  <div class="abs feature" style="top:1832px">
    <span class="feature-ring"><svg viewBox="0 0 40 40"><rect x="4" y="12" width="22" height="18" rx="2" fill="#fff"/><path d="M26 17h6l5 6v7H26z" fill="#fff"/><path d="M15 15v12M9 21h12" stroke="#f07c30" stroke-width="3"/><circle cx="11" cy="32" r="3" fill="#fff"/><circle cx="30" cy="32" r="3" fill="#fff"/></svg></span>
    <span class="feature-text">TrelTutoring for education.</span>
  </div>

  <div class="abs mark" style="left:92px;top:2180px"></div>
  <h2 class="abs h2" style="left:90px;top:2220px;font-size:35px;line-height:46px;width:600px">Supporting you creating your own outdoor activity and events.</h2>
  <p class="abs body-text" style="left:90px;top:2317px;width:590px">myTrelWave is focused on helping you to improving the health and well-being of your customers, friends, family or groups helping them become more active. We are passionate to work with all age groups but in particular the young person in appreciating and gaining the benefits of the outdoors.</p>
  <div class="abs btn" style="left:90px;top:2477px;width:182px">Read More <svg viewBox="0 0 16 16"><circle cx="8" cy="8" r="8" fill="#fff"/><path d="M4 8h7M8 5l3 3-3 3" stroke="#f07c30" stroke-width="1.8" fill="none"/></svg></div>
  <div class="abs btn ghost" style="left:287px;top:2477px;width:180px">Get In Touch <svg viewBox="0 0 16 16"><circle cx="8" cy="8" r="8" fill="#f07c30"/><path d="M4 8h7M8 5l3 3-3 3" stroke="#fff" stroke-width="1.8" fill="none"/></svg></div>

  <div class="abs mark" style="left:585px;top:2697px"></div>
  <h2 class="abs h2" style="left:0;top:2739px;width:1200px;text-align:center;font-size:37px">What are we working on?</h2>

  <article class="abs card" style="left:90px">
    <div class="card-media" role="img" aria-label="Photo: family walking along a woodland path" style="background:linear-gradient(180deg,#7a9a5a,#4e6a3a 55%,#8a8470)"></div>
    <h3 class="card-title">Get-me-Moving Campaign</h3>
    <p class="card-text">We are working on a national campaign to motivate people to be more active and take an interest in their daily activity.</p>
    <p class="card-link">Read More</p>
  </article>
  <article class="abs card" style="left:436px">
    <div class="card-media" role="img" aria-label="Photo: red squirrel display at a visitor centre" style="background:linear-gradient(135deg,#c85a3a,#a8503a 40%,#d8d0c4 70%,#5a4a3a)"></div>
    <h3 class="card-title">The story of the Red Squirrels</h3>
    <p class="card-text">The plight of the squirrel We are working on telling the story of the plight of the red squirrel creating education-al adventures in the areas red squirrels</p>
    <p class="card-link">Read More</p>
  </article>
  <article class="abs card" style="left:782px">
    <div class="card-media" role="img" aria-label="Photo: view over a forest and loch" style="background:linear-gradient(180deg,#b8c4d0,#8a9aa8 35%,#3e5a3a 60%,#5a6a3a)"></div>
    <h3 class="card-title">A forest for a 1000 years</h3>
    <p class="card-text">Alderwick Forest Alderwick Forest is a fantastic location found on the side of Loch Fennard and provides walks and opportunities to experience the nature and a natural</p>
    <p class="card-link">Read More</p>
  </article>

  <div class="abs foot-brand"><span class="brand-dot"></span><span class="brand-name">TrelWave</span></div>

  <h4 class="abs foot-h" style="left:90px;top:3534px">QUICK LINKS</h4>
  <ul class="abs quick" style="left:92px;top:3574px">
    <li>Home</li><li>Projects</li><li>What we do</li><li>Contact</li><li>My Trel Adventure Platform</li>
  </ul>

  <h4 class="abs foot-h" style="left:375px;top:3534px">CONTACT US</h4>
  <div class="abs" style="left:377px;top:3575px">
    <div class="contact-row"><svg viewBox="0 0 13 13"><path d="M6.5 0a4.5 4.5 0 0 0-4.5 4.5C2 8 6.5 13 6.5 13S11 8 11 4.5A4.5 4.5 0 0 0 6.5 0z" fill="#fff"/><circle cx="6.5" cy="4.5" r="1.7" fill="#262626"/></svg><span>1820 Harlow Lane Brindleford<br>AL 35990</span></div>
    <div class="contact-row"><svg viewBox="0 0 13 13"><path d="M2 1c.6-.6 1.3-.6 1.8 0l1.4 1.9c.4.6.2 1.2-.3 1.6l-.6.5c.6 1.4 1.8 2.6 3.2 3.2l.5-.6c.4-.5 1-.7 1.600-.3l1.9 1.4c.6.5.6 1.2 0 1.8l-.9.9C7.7 12 1 5.3 1.1 2.4z" fill="#fff"/></svg><span>Phone : 555 014 2730</span></div>
    <div class="contact-row"><svg viewBox="0 0 13 13"><rect x="0" y="2" width="13" height="9" fill="#fff"/><path d="M0 2l6.5 5L13 2" stroke="#262626" stroke-width="1.2" fill="none"/></svg><span>Email : hello@mytrelquestly.example</span></div>
  </div>

  <h4 class="abs foot-h" style="left:702px;top:3531px">GET IN TOUCH</h4>
  <p class="abs" style="left:703px;top:3576px;font-size:12.5px;color:#fff">Alternatively You Can Fill In the Following Contact Form:</p>
  <div class="abs field" style="left:704px;top:3618px;width:197px">NAME</div>
  <div class="abs field" style="left:913px;top:3618px;width:197px">EMAIL</div>
  <div class="abs field" style="left:704px;top:3673px;width:197px">PHONE</div>
  <div class="abs submit" style="left:913px;top:3673px;width:197px">Submit</div>

  <p class="abs copyright">Copyright © 2019. All Rights Reserved</p>
</div>
</body>
</html>
```